Property Management Company Business Cards

Need business cards for a property management company located in Michigan. We manage houses for clients all over the world. Young and modern company, looking for eye catching design. Please work with the attached logo.

Industry/Entity Type

Property Management

Requirements
Must have
• Need lines for address, telephone number, fax number, web site.

Also lines for name, and job title

```html
<!DOCTYPE html>
<html lang="en">
<head>
<meta charset="utf-8">
<title>Lakeshore Crest Management – Business Cards</title>
<link rel="stylesheet" href="https://fonts.googleapis.com/css2?family=Arimo:wght@400;700&family=Open+Sans:wght@700&display=swap">
<style>
  :root {
    --backdrop: #2b2b2d;
    --card: #ffffff;
    --ink: #3b3b3e;
    --accent: #29a8e0;
    --band-text: #ffffff;
  }
  * { box-sizing: border-box; margin: 0; padding: 0; }
  html, body { width: 1200px; height: 757px; overflow: hidden; }
  body {
    background: var(--backdrop);
    font-family: "Arimo", Arial, sans-serif;
    position: relative;
  }
  .card {
    position: absolute;
    top: 228px;
    width: 520px;
    height: 300px;
    background: var(--card);
    border-radius: 26px;
    overflow: hidden;
  }
  .card--front { left: 50px; }
  .card--back { left: 630px; }

  /* Front */
  .brand {
    position: absolute;
    left: 44px;
    top: 44px;
    display: flex;
    align-items: center;
    gap: 12px;
  }
  .brand__dot {
    width: 30px; height: 30px;
    border-radius: 50%;
    background: var(--accent);
  }
  .brand__name {
    font-family: "Open Sans", Arial, sans-serif;
    font-weight: 700;
    font-size: 23px;
    color: var(--ink);
    letter-spacing: 0.2px;
  }
  .holder {
    position: absolute;
    left: 44px;
    top: 124px;
    color: var(--ink);
    font-size: 15px;
  }
  .holder__name {
    color: var(--accent);
    font-weight: 700;
    font-size: 20px;
  }
  .contacts {
    position: absolute;
    left: 44px;
    top: 168px;
    list-style: none;
    color: var(--ink);
    font-size: 14px;
    line-height: 21px;
  }
  .contacts li { display: flex; align-items: center; gap: 7px; }
  .contacts svg { width: 11px; height: 11px; fill: var(--ink); }
  .band {
    position: absolute;
    left: 0; bottom: 0;
    width: 520px; height: 80px;
  }
  .band__address {
    position: absolute;
    left: 44px;
    bottom: 14px;
    color: var(--band-text);
    font-size: 13px;
  }
  .corner-mark {
    position: absolute;
    right: 34px;
    top: 152px;
    width: 62px; height: 62px;
    border-radius: 50%;
    background: var(--accent);
    border: 5px solid var(--card);
  }

  /* Back */
  .back-brand {
    position: absolute;
    left: 0; right: 0;
    top: 92px;
    display: flex;
    flex-direction: column;
    align-items: center;
    gap: 16px;
  }
  .back-brand__dot {
    width: 56px; height: 56px;
    border-radius: 50%;
    background: var(--accent);
  }
  .back-brand__name {
    font-family: "Open Sans", Arial, sans-serif;
    font-weight: 700;
    font-size: 24px;
    color: var(--ink);
  }
  .back-web {
    position: absolute;
    left: 0; right: 0;
    bottom: 44px;
    text-align: center;
    color: var(--ink);
    font-size: 19px;
    letter-spacing: 1.5px;
  }
</style>
</head>
<body>

<section class="card card--front">
  <div class="brand">
    <span class="brand__dot"></span>
    <span class="brand__name">LAKESHORE CREST MANAGEMENT</span>
  </div>

  <p class="holder"><span class="holder__name">Your Name,</span> Title</p>

  <ul class="contacts">
    <li>
      <svg viewBox="0 0 12 12" aria-hidden="true"><path d="M2.5 0.5 4.5 3 3.5 4.3a6 6 0 0 0 4.2 4.2L9 7.5l2.5 2-1 2C5 11.5.5 7 .5 1.5z"/></svg>
      123-456-789
    </li>
    <li>
      <svg viewBox="0 0 12 12" aria-hidden="true"><path d="M2 4h8v5H2z M3 1h6v3H3z M3 9h6v2H3z"/></svg>
      123-456-789
    </li>
    <li>
      <svg viewBox="0 0 12 12" aria-hidden="true"><circle cx="6" cy="6" r="5.5" fill="none" stroke="#3b3b3e" stroke-width="1"/><path d="M0.5 6h11M6 .5v11" stroke="#3b3b3e" stroke-width="1"/></svg>
      www.website.com
    </li>
  </ul>

  <svg class="band" viewBox="0 0 520 80" preserveAspectRatio="none" aria-hidden="true">
    <path d="M0 40 Q 260 30 520 0 L520 80 L0 80 Z" fill="var(--accent)"/>
  </svg>
  <p class="band__address">Street Name, City Name, State City Zip Code</p>

  <span class="corner-mark"></span>
</section>

<section class="card card--back">
  <div class="back-brand">
    <span class="back-brand__dot"></span>
    <span class="back-brand__name">LAKESHORE CREST MANAGEMENT</span>
  </div>
  <p class="back-web">www.website.com</p>
</section>

</body>
</html>
```